Web App Dashboard Design for Healthcare Company

We have developed a simple web application with 3 navigation menus. We like the current design (very much modeled after Ledgerly), but we want to explore UI options for the branding, header, menus, and footer that we may not have considered.

The attached screenshots show the layout and two menu "hover" views as they currently exist.

This web application is used by employees only.

Menu 1 - Module Menu:
Allows the user to switch easily between Account, Employee, and Care Management.

Menu 2 - Reports Menu
Allows user to view available reports within each Module.

Menu 3 - Admin Menu
Allows the user to easily create new content types within each module.

Use our branded colors and font.

Colors:
Logo Blue (dark): 00c0f3
Logo Blue (light): 44c8f5
Nav Blue: 0994d0
Green: 71b44b
Grayscale: (not specified)

Font:
Lato (Google Font)

Target Market(s)

Internal staff.

Industry/Entity Type

Healthcare

Number of Pages Required

3 page

Font styles to use
Sans Serif
Other font styles liked:
• Lato (Google Font)

Colors
0293ce
9bcb3c

Requirements
Must have
• It's really a one page design, but we want to see the two "hover" views for the Module Menu and the Admin Menu.
• It should also be very clear which "Report" page the user is on (the active menu link).
• Must use branded colors, font, and logo.
• Logo Blue (dark): 00c0f3
• Logo Blue (light): 44c8f5
• Nav Blue: 0994d0
• Green: 71b44b
• Grayscale: Designer may choose
Nice to have
• It would be nice to have simple uncluttered payouts.
Should not have
• The design should not have menu options exposed by default.

```html
<!DOCTYPE html>
<html lang="en">
<head>
<meta charset="utf-8">
<title>Tendwell – Web App Design</title>
<link rel="stylesheet" href="https://fonts.googleapis.com/css2?family=Lato:wght@300;400;700&family=Dosis:wght@300;400&display=swap">
<style>
:root{
  --board:#7786a8;
  --nav-blue:#0994d0;
  --logo-blue:#00c0f3;
  --green:#71b44b;
  --red:#e8262c;
  --side:#1b1e22;
  --side-dark:#16181b;
  --side-active:#1d2a33;
  --side-text:#b9bec4;
  --ink:#2b2f33;
  --row-alt:#eeeeee;
  --line:#d6d6d6;
  --white:#ffffff;
}
*{box-sizing:border-box;margin:0;padding:0}
html,body{width:670px;height:1200px;overflow:hidden;background:var(--board)}
body{font-family:"Lato",sans-serif;color:var(--ink)}
.board{position:relative;width:670px;height:1200px;background:var(--board);overflow:hidden}
.screen{position:absolute;left:10px;width:651px;height:367px;background:var(--white);overflow:hidden}
.s1{top:10px}.s2{top:387px}.s3{top:764px}

.topbar{position:absolute;left:0;top:0;width:100%;height:34px;border-bottom:1px solid var(--line);background:var(--white)}
.brand{position:absolute;left:18px;top:10px;display:flex;align-items:center;gap:4px;font-weight:700;font-size:10px;color:var(--ink)}
.brand-dot{width:8px;height:8px;border-radius:50%;background:var(--logo-blue)}
.user{position:absolute;right:18px;top:5px;display:flex;align-items:center;gap:8px;font-size:9px}
.avatar{width:24px;height:24px;border-radius:50%;background:linear-gradient(135deg,#e8c9a8,#b98a63)}

.sidebar{position:absolute;left:0;top:34px;width:134px;bottom:0;background:var(--side)}
.module{position:absolute;left:10px;top:21px;font-size:9.5px;color:var(--green)}
.module::after{content:"";display:inline-block;width:4px;height:4px;border-right:1px solid var(--green);border-bottom:1px solid var(--green);transform:rotate(45deg);margin-left:5px;vertical-align:3px}
.module-rule{position:absolute;left:0;top:59px;width:134px;height:1px;background:#2c3036}
.nav{position:absolute;left:0;width:134px;height:28px;display:flex;align-items:center;gap:10px;padding-left:16px;font-size:7.5px;color:var(--side-text)}
.nav svg{width:11px;height:11px;stroke:var(--side-text);fill:none;stroke-width:1.2}
.nav.active{background:var(--side-active);color:var(--nav-blue)}
.nav.active svg{stroke:var(--nav-blue)}
.n1{top:86px}.n2{top:115px}.n3{top:143px}.n4{top:172px}.n5{top:201px}
.foot-band{position:absolute;left:0;bottom:0;width:134px;height:28px;background:var(--side-dark);display:flex;align-items:center;gap:9px;padding-left:16px;font-size:7.5px;color:var(--red)}
.foot-band svg{width:11px;height:11px;stroke:var(--red);fill:none;stroke-width:1.4}
.foot-band.center{justify-content:center;padding-left:0}

.fab{position:absolute;left:120px;top:80px;width:28px;height:28px;border-radius:50%;display:flex;align-items:center;justify-content:center;z-index:3;box-shadow:0 1px 3px rgba(0,0,0,.3)}
.fab svg{width:12px;height:12px;stroke:var(--white);stroke-width:2.2}
.fab.add{background:var(--green)}
.fab.close{background:var(--red)}

.popup{position:absolute;left:133px;top:88px;width:133px;height:134px;background:#1d2025;border-radius:4px;box-shadow:0 3px 10px rgba(0,0,0,.45);z-index:2}
.pop-item{position:absolute;left:0;width:133px;height:28px;display:flex;align-items:center;gap:11px;padding-left:14px;font-size:7.5px;color:var(--side-text)}
.pop-item svg{width:11px;height:11px;stroke:var(--side-text);fill:none;stroke-width:1.2}
.pop-item.active{background:var(--side-active);color:var(--nav-blue)}
.pop-item.active svg{stroke:var(--nav-blue)}
.p1{top:16px}.p2{top:44px}.p3{top:73px}.p4{top:102px}

.mod-card{position:absolute;left:10px;width:114px;height:57px;border:1px solid #4a4f56;border-radius:3px;display:flex;flex-direction:column;align-items:center;justify-content:center;gap:5px;font-size:7px;color:var(--side-text)}
.mod-card svg{width:24px;height:24px;fill:none;stroke:var(--side-text);stroke-width:1.3}
.mod-card.active{border-color:var(--green);color:var(--green)}
.mod-card.active svg{stroke:var(--green)}
.m1{top:60px}.m2{top:128px}.m3{top:194px}

.tabs{position:absolute;left:173px;top:40px;height:14px;font-size:6.5px;color:#3b3f44}
.tab{position:absolute;top:0;white-space:nowrap;letter-spacing:.2px}
.tab.active{color:var(--green);border-bottom:1px solid var(--green);padding:0 3px 5px;left:-3px}
.t2{left:62px}.t3{left:121px}.t4{left:205px}.t5{left:256px}

.table{position:absolute;left:152px;top:61px;width:480px;border:1px solid var(--line);border-top:none}
.thead,.row{position:relative;height:24px;font-size:7.5px}
.thead{background:var(--nav-blue);color:var(--white);font-size:8px}
.row:nth-child(odd){background:var(--row-alt)}
.thead span,.row span{position:absolute;top:0;line-height:24px;white-space:nowrap}
.thead span:nth-child(1),.row span:nth-child(1){left:10px}
.thead span:nth-child(2),.row span:nth-child(2){left:98px}
.thead span:nth-child(3),.row span:nth-child(3){left:154px}
.thead span:nth-child(4),.row span:nth-child(4){left:194px}
.thead span:nth-child(5),.row span:nth-child(5){left:284px}
.thead span:nth-child(6),.row span:nth-child(6){left:349px}
.thead span:nth-child(7),.row span:nth-child(7){left:412px}
.row .ok,.row .no{top:6px;width:11px;height:11px;border-radius:50%;line-height:11px;text-align:center;color:var(--white);font-size:7px;font-weight:700}
.row .ok{background:#3fb356}
.row .ok::after{content:"✓"}
.row .no{background:var(--red)}
.row .no::after{content:"✕";font-size:6px}

.pager{position:absolute;left:338px;top:331px;display:flex;align-items:center;gap:0;font-size:8px;color:#666}
.pg-btn{width:15px;height:15px;border-radius:50%;background:var(--nav-blue);display:flex;align-items:center;justify-content:center}
.pg-btn svg{width:7px;height:7px;stroke:var(--white);stroke-width:2;fill:none}
.pg-num{width:14.5px;text-align:center}
.pg-num.current{color:var(--nav-blue)}
.pages{display:flex;margin:0 10px 0 14px}

.legal{position:absolute;left:0;right:0;padding-left:134px;top:357px;text-align:center;font-size:5px;color:#888}
.legal a{color:var(--nav-blue);text-decoration:none}

.showcase-brand{position:absolute;left:24px;top:1158px;display:flex;align-items:center;gap:6px;font-size:17px;font-weight:700;color:var(--white)}
.showcase-brand .brand-dot{width:12px;height:12px}
.showcase-title{position:absolute;left:0;width:670px;top:1150px;text-align:center;font-family:"Dosis",sans-serif;font-weight:300;font-size:27px;color:#f1f3f7;letter-spacing:.5px}
</style>
</head>
<body>
<div class="board">

<!-- Screen 1: default view -->
<section class="screen s1">
  <header class="topbar">
    <div class="brand"><span class="brand-dot"></span>Tendwell</div>
    <div class="user">Dana<div class="avatar" role="img" aria-label="User profile photo"></div></div>
  </header>
  <aside class="sidebar">
    <div class="module">Accounts Management</div>
    <div class="module-rule"></div>
    <div class="nav n1"><svg viewBox="0 0 12 12"><path d="M3 8V5a3 3 0 016 0v3l1 1H2zM5 10.5h2"/></svg>Reminders</div>
    <div class="nav n2"><svg viewBox="0 0 12 12"><rect x="1" y="2" width="10" height="8"/><circle cx="6" cy="5.5" r="1.5"/><path d="M3.5 9a2.5 2 0 015 0"/></svg>Accounts</div>
    <div class="nav n3"><svg viewBox="0 0 12 12"><path d="M2 3h8v5H5L3 10V8H2z"/></svg>Patient Requests</div>
    <div class="nav n4 active"><svg viewBox="0 0 12 12"><rect x="1" y="2" width="10" height="7"/><path d="M4 11h4M3 7l2-2 2 1 2-2"/></svg>Reports</div>
    <div class="nav n5"><svg viewBox="0 0 12 12"><rect x="2" y="1" width="6" height="10"/><path d="M8 5h2v6H8M4 3h2M4 5h2M4 7h2"/></svg>My Company</div>
    <div class="foot-band"><svg viewBox="0 0 12 12"><path d="M6 1v5M3.5 3a4 4 0 105 0"/></svg>Sign Out</div>
  </aside>
  <div class="fab add"><svg viewBox="0 0 12 12"><path d="M6 1v10M1 6h10"/></svg></div>
  <nav class="tabs"><span class="tab active">REMINDERS</span><span class="tab t2">ACCOUNTS</span><span class="tab t3">PATIENT REQUESTS</span><span class="tab t4">REPORTS</span><span class="tab t5">MY COMPANY</span></nav>
  <div class="table">
    <div class="thead"><span>Sample Text</span><span>Label Two</span><span>Tab</span><span>Random Message</span><span>Caption</span><span>Testing</span><span>Last Column</span></div>
    <div class="rows">
      <div class="row"><span>Lorem ipsum</span><span>One</span><span class="ok"></span><span>Etiam risus lorem</span><span>1Caption</span><span></span><span>Completed</span></div>
      <div class="row"><span>Integer vulputate</span><span>Two</span><span class="ok"></span><span>Praesent id justo</span><span>2Caption</span><span>Testing</span><span>Completed</span></div>
      <div class="row"><span>Lorem ipsum</span><span>Three</span><span class="no"></span><span>Etiam risus lorem</span><span>3Caption</span><span></span><span>Missed</span></div>
      <div class="row"><span>Integer vulputate</span><span>Four</span><span class="ok"></span><span>Praesent id justo</span><span>4Caption</span><span>Testing</span><span>Completed</span></div>
      <div class="row"><span>Integer vulputate</span><span>Five</span><span class="no"></span><span></span><span>5Caption</span><span>Testing</span><span>Missed</span></div>
      <div class="row"><span>Integer vulputate</span><span>Six</span><span class="no"></span><span>Etiam risus lorem</span><span>6Caption</span><span></span><span>Missed</span></div>
      <div class="row"><span>Lorem ipsum</span><span>Seven</span><span class="ok"></span><span>Praesent id justo</span><span>7Caption</span><span>Testing</span><span>Completed</span></div>
      <div class="row"><span>Integer vulputate</span><span>Eight</span><span class="ok"></span><span>Etiam risus lorem</span><span>8Caption</span><span></span><span>Completed</span></div>
      <div class="row"><span>Lorem ipsum</span><span>Nine</span><span class="ok"></span><span></span><span>9Caption</span><span>Testing</span><span>Completed</span></div>
      <div class="row"><span>Integer vulputate</span><span>Ten</span><span class="no"></span><span>Praesent id justo</span><span>10Caption</span><span>Testing</span><span>Missed</span></div>
    </div>
  </div>
  <div class="pager"><span class="pg-btn"><svg viewBox="0 0 8 8"><path d="M5 1L2 4l3 3"/></svg></span><div class="pages"><span class="pg-num">1</span><span class="pg-num current">2</span><span class="pg-num">3</span><span class="pg-num">4</span><span class="pg-num">5</span></div><span class="pg-btn"><svg viewBox="0 0 8 8"><path d="M3 1l3 3-3 3"/></svg></span></div>
  <footer class="legal">Tendwell™ | Copyright © 2016. All Rights Reserved. <a>Get Started</a> | <a>About Us</a> | <a>Contact Us</a> | <a>Terms &amp; Agreement</a> | <a>Privacy Policy</a></footer>
</section>

<!-- Screen 2: admin menu open -->
<section class="screen s2">
  <header class="topbar">
    <div class="brand"><span class="brand-dot"></span>Tendwell</div>
    <div class="user">Dana<div class="avatar" role="img" aria-label="User profile photo"></div></div>
  </header>
  <aside class="sidebar">
    <div class="module">Accounts Management</div>
    <div class="module-rule"></div>
    <div class="nav n1"><svg viewBox="0 0 12 12"><path d="M3 8V5a3 3 0 016 0v3l1 1H2zM5 10.5h2"/></svg>Reminders</div>
    <div class="nav n2"><svg viewBox="0 0 12 12"><rect x="1" y="2" width="10" height="8"/><circle cx="6" cy="5.5" r="1.5"/><path d="M3.5 9a2.5 2 0 015 0"/></svg>Accounts</div>
    <div class="nav n3"><svg viewBox="0 0 12 12"><path d="M2 3h8v5H5L3 10V8H2z"/></svg>Patient Requests</div>
    <div class="nav n4 active"><svg viewBox="0 0 12 12"><rect x="1" y="2" width="10" height="7"/><path d="M4 11h4M3 7l2-2 2 1 2-2"/></svg>Reports</div>
    <div class="nav n5"><svg viewBox="0 0 12 12"><rect x="2" y="1" width="6" height="10"/><path d="M8 5h2v6H8M4 3h2M4 5h2M4 7h2"/></svg>My Company</div>
    <div class="foot-band"><svg viewBox="0 0 12 12"><path d="M6 1v5M3.5 3a4 4 0 105 0"/></svg>Sign Out</div>
  </aside>
  <div class="fab close"><svg viewBox="0 0 12 12"><path d="M2 2l8 8M10 2l-8 8"/></svg></div>
  <div class="popup">
    <div class="pop-item p1"><svg viewBox="0 0 12 12"><rect x="1" y="2" width="10" height="8"/><circle cx="6" cy="5.5" r="1.5"/><path d="M3.5 9a2.5 2 0 015 0"/></svg>Account</div>
    <div class="pop-item p2"><svg viewBox="0 0 12 12"><rect x="2" y="1" width="6" height="10"/><path d="M8 5h2v6H8M4 3h2M4 5h2M4 7h2"/></svg>Company Contact</div>
    <div class="pop-item p3 active"><svg viewBox="0 0 12 12"><rect x="2" y="2" width="8" height="9"/><path d="M4 1v2M8 1v2M4 6h4M4 8h3"/></svg>Note</div>
    <div class="pop-item p4"><svg viewBox="0 0 12 12"><path d="M1.5 2h9v6h-5L3 10V8H1.5z"/><path d="M3.5 4.5h5M3.5 6h3"/></svg>Message</div>
  </div>
  <nav class="tabs"><span class="tab active">REMINDERS</span><span class="tab t2">ACCOUNTS</span><span class="tab t3">PATIENT REQUESTS</span><span class="tab t4">REPORTS</span><span class="tab t5">MY COMPANY</span></nav>
  <div class="table">
    <div class="thead"><span>Sample Text</span><span>Label Two</span><span>Tab</span><span>Random Message</span><span>Caption</span><span>Testing</span><span>Last Column</span></div>
    <div class="rows">
      <div class="row"><span>Lorem ipsum</span><span>One</span><span class="ok"></span><span>Etiam risus lorem</span><span>1Caption</span><span></span><span>Completed</span></div>
      <div class="row"><span>Integer vulputate</span><span>Two</span><span class="ok"></span><span>Praesent id justo</span><span>2Caption</span><span>Testing</span><span>Completed</span></div>
      <div class="row"><span>Lorem ipsum</span><span>Three</span><span class="no"></span><span>Etiam risus lorem</span><span>3Caption</span><span></span><span>Missed</span></div>
      <div class="row"><span>Integer vulputate</span><span>Four</span><span class="ok"></span><span>Praesent id justo</span><span>4Caption</span><span>Testing</span><span>Completed</span></div>
      <div class="row"><span>Integer vulputate</span><span>Five</span><span class="no"></span><span></span><span>5Caption</span><span>Testing</span><span>Missed</span></div>
      <div class="row"><span>Integer vulputate</span><span>Six</span><span class="no"></span><span>Etiam risus lorem</span><span>6Caption</span><span></span><span>Missed</span></div>
      <div class="row"><span>Lorem ipsum</span><span>Seven</span><span class="ok"></span><span>Praesent id justo</span><span>7Caption</span><span>Testing</span><span>Completed</span></div>
      <div class="row"><span>Integer vulputate</span><span>Eight</span><span class="ok"></span><span>Etiam risus lorem</span><span>8Caption</span><span></span><span>Completed</span></div>
      <div class="row"><span>Lorem ipsum</span><span>Nine</span><span class="ok"></span><span></span><span>9Caption</span><span>Testing</span><span>Completed</span></div>
      <div class="row"><span>Integer vulputate</span><span>Ten</span><span class="no"></span><span>Praesent id justo</span><span>10Caption</span><span>Testing</span><span>Missed</span></div>
    </div>
  </div>
  <div class="pager"><span class="pg-btn"><svg viewBox="0 0 8 8"><path d="M5 1L2 4l3 3"/></svg></span><div class="pages"><span class="pg-num">1</span><span class="pg-num current">2</span><span class="pg-num">3</span><span class="pg-num">4</span><span class="pg-num">5</span></div><span class="pg-btn"><svg viewBox="0 0 8 8"><path d="M3 1l3 3-3 3"/></svg></span></div>
  <footer class="legal">Tendwell™ | Copyright © 2016. All Rights Reserved. <a>Get Started</a> | <a>About Us</a> | <a>Contact Us</a> | <a>Terms &amp; Agreement</a> | <a>Privacy Policy</a></footer>
</section>

<!-- Screen 3: module menu open -->
<section class="screen s3">
  <header class="topbar">
    <div class="brand"><span class="brand-dot"></span>Tendwell</div>
    <div class="user">Dana<div class="avatar" role="img" aria-label="User profile photo"></div></div>
  </header>
  <aside class="sidebar">
    <div class="mod-card m1 active"><svg viewBox="0 0 24 24"><circle cx="11" cy="7" r="4.5"/><path d="M3 21c0-5 3.5-8 8-8s8 3 8 8z"/><path d="M13 18l2.5 2.5L21 15"/></svg>Accounts Management</div>
    <div class="mod-card m2"><svg viewBox="0 0 24 24"><circle cx="10" cy="7" r="4.5"/><path d="M2 21c0-5 3.5-8 8-8s8 3 8 8z"/><path d="M15 3.5a4.5 4.5 0 010 8M18 14c2.5 1 4 3.5 4 7h-3"/></svg>Employee Management</div>
    <div class="mod-card m3"><svg viewBox="0 0 24 24"><path d="M12 12s-5-3-5-6.5A2.7 2.7 0 0112 4a2.7 2.7 0 015 1.5C17 9 12 12 12 12z"/><path d="M2 16l5-2h5a1.5 1.5 0 010 3H9M12 17l6-3a1.5 1.5 0 012 2l-7 4H6l-4 1"/></svg>Care Management</div>
    <div class="foot-band center">CANCEL</div>
  </aside>
  <nav class="tabs"><span class="tab active">REMINDERS</span><span class="tab t2">ACCOUNTS</span><span class="tab t3">PATIENT REQUESTS</span><span class="tab t4">REPORTS</span><span class="tab t5">MY COMPANY</span></nav>
  <div class="table">
    <div class="thead"><span>Sample Text</span><span>Label Two</span><span>Tab</span><span>Random Message</span><span>Caption</span><span>Testing</span><span>Last Column</span></div>
    <div class="rows">
      <div class="row"><span>Lorem ipsum</span><span>One</span><span class="ok"></span><span>Etiam risus lorem</span><span>1Caption</span><span></span><span>Completed</span></div>
      <div class="row"><span>Integer vulputate</span><span>Two</span><span class="ok"></span><span>Praesent id justo</span><span>2Caption</span><span>Testing</span><span>Completed</span></div>
      <div class="row"><span>Lorem ipsum</span><span>Three</span><span class="no"></span><span>Etiam risus lorem</span><span>3Caption</span><span></span><span>Missed</span></div>
      <div class="row"><span>Integer vulputate</span><span>Four</span><span class="ok"></span><span>Praesent id justo</span><span>4Caption</span><span>Testing</span><span>Completed</span></div>
      <div class="row"><span>Integer vulputate</span><span>Five</span><span class="no"></span><span></span><span>5Caption</span><span>Testing</span><span>Missed</span></div>
      <div class="row"><span>Integer vulputate</span><span>Six</span><span class="no"></span><span>Etiam risus lorem</span><span>6Caption</span><span></span><span>Missed</span></div>
      <div class="row"><span>Lorem ipsum</span><span>Seven</span><span class="ok"></span><span>Praesent id justo</span><span>7Caption</span><span>Testing</span><span>Completed</span></div>
      <div class="row"><span>Integer vulputate</span><span>Eight</span><span class="ok"></span><span>Etiam risus lorem</span><span>8Caption</span><span></span><span>Completed</span></div>
      <div class="row"><span>Lorem ipsum</span><span>Nine</span><span class="ok"></span><span></span><span>9Caption</span><span>Testing</span><span>Completed</span></div>
      <div class="row"><span>Integer vulputate</span><span>Ten</span><span class="no"></span><span>Praesent id justo</span><span>10Caption</span><span>Testing</span><span>Missed</span></div>
    </div>
  </div>
  <div class="pager"><span class="pg-btn"><svg viewBox="0 0 8 8"><path d="M5 1L2 4l3 3"/></svg></span><div class="pages"><span class="pg-num">1</span><span class="pg-num current">2</span><span class="pg-num">3</span><span class="pg-num">4</span><span class="pg-num">5</span></div><span class="pg-btn"><svg viewBox="0 0 8 8"><path d="M3 1l3 3-3 3"/></svg></span></div>
  <footer class="legal">Tendwell™ | Copyright © 2016. All Rights Reserved. <a>Get Started</a> | <a>About Us</a> | <a>Contact Us</a> | <a>Terms &amp; Agreement</a> | <a>Privacy Policy</a></footer>
</section>

<div class="showcase-brand"><span class="brand-dot"></span>Tendwell</div>
<div class="showcase-title">Web App Design</div>

</div>
</body>
</html>
```